Label design for Japanese sake bottle (American market targeted)

We are launching a new sake product and the product concept is as below.

1. It is a draft which means it has a fresh taste
2. We want to emphasize on its cleanness and that it's easy drinkable
3. It is most likely to have a light blue transparent 300ml bottle
4. Product name is "Clear Hollow Brew" although you don't have to make them stand out on the label. We are targeting non-Japanese customers, so all we want them to know is that "it is a sake and easy drinkable"
5. It is affordable. Its retail price per bottle would be somewhere around $10

Target Market(s)

Non-Japanese, preferably non-Asian liquor / grocery stores and restaurants

Industry/Entity Type

Glass Bottle

Font styles to use
Serif
Sans Serif
Decorative

Colors

Designer to choose colors to be used in the design.

Requirements
Must have
• The word "sake"
• Pureness, cleanness
Nice to have
• Any ideas for entering non-Asian market will be welcome!
Should not have
• Please do NOT make it similar to our competitors (which I would attach a few images of)

```html
<!DOCTYPE html>
<html lang="en">
<head>
<meta charset="utf-8">
<title>Clear Hollow Brew – Sake Label</title>
<link href="https://fonts.googleapis.com/css2?family=Montserrat:wght@500;600;700;800&display=swap" rel="stylesheet">
<style>
  :root {
    --page-bg: #eef1f4;
    --label-white: #ffffff;
    --ink-navy: #1c2758;
    --silver: #c9cbce;
    --silver-light: #e4e5e7;
    --wash-blue: #4b61c4;
    --wash-blue-deep: #3a4fae;
    --text-on-wash: #ffffff;
  }
  * { margin: 0; padding: 0; box-sizing: border-box; }
  html, body {
    width: 1200px; height: 1200px; overflow: hidden;
    background: var(--page-bg);
    font-family: "Montserrat", sans-serif;
  }
  .canvas { position: relative; width: 1200px; height: 1200px; }
  .label {
    position: absolute; left: 120px; top: 220px;
    width: 960px; height: 760px;
    background: var(--label-white);
    box-shadow: 0 2px 14px rgba(28, 39, 88, 0.08);
    overflow: hidden;
  }
  .label-edge-top {
    position: absolute; left: 0; right: 0; top: 0; height: 12px;
    background: linear-gradient(90deg, var(--silver-light), var(--silver), var(--silver-light));
  }
  .label-edge-bottom {
    position: absolute; left: 0; right: 0; bottom: 26px; height: 16px;
    background: linear-gradient(90deg, var(--silver-light), var(--silver), var(--silver-light));
  }
  .rule-top {
    position: absolute; left: 226px; top: 64px; width: 410px; height: 10px;
    background: var(--silver-light);
  }
  .rule-bottom {
    position: absolute; left: 226px; top: 170px; width: 410px; height: 12px;
    background: var(--silver-light);
  }
  .style-line {
    position: absolute; left: 226px; top: 50px;
    font-size: 25px; font-weight: 700; letter-spacing: 2px;
    color: var(--ink-navy); white-space: nowrap;
  }
  .style-line span { position: relative; background: var(--label-white); padding-right: 10px; }
  .product-word {
    position: absolute; left: 222px; top: 82px;
    font-size: 98px; font-weight: 800; letter-spacing: 8px;
    color: var(--ink-navy); line-height: 1;
  }
  .category-word {
    position: absolute; left: 690px; top: 200px;
    height: 480px;
    writing-mode: vertical-rl;
    transform: rotate(180deg);
    font-size: 128px; font-weight: 700; letter-spacing: 22px;
    line-height: 1; color: var(--ink-navy);
    text-align: center;
  }
  .brand-mark {
    position: absolute; left: 222px; top: 258px;
    display: flex; align-items: center; gap: 10px; z-index: 2;
  }
  .brand-mark .dot {
    width: 34px; height: 34px; border-radius: 50%;
    background: var(--wash-blue-deep);
  }
  .brand-mark .name {
    font-size: 22px; font-weight: 700; letter-spacing: 2px;
    color: var(--ink-navy);
  }
  .wash {
    position: absolute; left: 262px; top: 300px;
    width: 310px; height: 300px;
  }
  .taste-notes {
    position: absolute; left: 262px; top: 300px;
    width: 310px; height: 300px;
    display: flex; align-items: center; justify-content: center;
    text-align: left;
    font-size: 38px; font-weight: 600; letter-spacing: 2px;
    line-height: 56px; color: var(--text-on-wash);
  }
</style>
</head>
<body>
<div class="canvas">
  <div class="label">
    <div class="label-edge-top"></div>

    <div class="rule-top"></div>
    <div class="style-line"><span>CLEAR HOLLOW</span></div>
    <div class="rule-bottom"></div>
    <div class="product-word">BREW</div>

    <div class="category-word">SAKE</div>

    <div class="brand-mark">
      <div class="dot"></div>
      <div class="name">KIYORA</div>
    </div>

    <svg class="wash" viewBox="0 0 310 300" role="img" aria-label="Hand-painted blue watercolour circle">
      <defs>
        <radialGradient id="washTone" cx="50%" cy="45%" r="60%">
          <stop offset="0%" stop-color="#5068cc"/>
          <stop offset="100%" stop-color="#3f55b8"/>
        </radialGradient>
      </defs>
      <ellipse cx="155" cy="150" rx="152" ry="146" fill="url(#washTone)"/>
    </svg>

    <div class="taste-notes"><div>FRESH<br>SMOOTH<br>CRISP</div></div>

    <div class="label-edge-bottom"></div>
  </div>
</div>
</body>
</html>
```